Regional health service needs a PowerPoint design

We are a new organisation responsible for the purchasing of health services for the population of Basildon and Brentwood in Essex, UK - a population of c.300,000.

We are looking for a set of powerpoint master slides for use principally as 'talk books' and reports for presenting information regarding the performance of the organisation externally and to use as the basis for producing internal reports and communications.

We would like to see designs which portray the organisation as being new and different from historic CHW organisations, whilst following the principles outlined within National CHW brand guidelines (see attached). The slides should communicate creativity and professionalism.

Our logo is available on request (due to technical issues, we cannot upload onto here).

Our brand guidelines are available at:
http://www.carewellmarks.example/all-guidelines/guidelines/authorised-clinical-commissioning-groups/introduction

An example report (which we would look to move over to our new template) is available at:
http://www.marrowfieldandkeltonhcb.example/key-documents/doc_download/142-integrated-plan-2013-15

Further information on us is available on our website: www.marrowfieldandkeltonhcb.example

Target Market(s)

Target audience is healthcare professionals and the general public.

Industry/Entity Type

Health

Requirements
Must have
• Include the organisations logo and provide a cover sheet front page and 3/4 slides showing how reports could be structured (e.g. narrative and graphical information / tabular information / use of photos etc).

Typefaces and colour schemes should be in line with our brand guidelines (i.e. principal use of Arial). Our guidelines are available at:

Nice to have
• As an organisation we are made up of four localities, it would be good to see designs that draw on this element of our organisation.

```html
<!DOCTYPE html>
<html lang="en">
<head>
<meta charset="utf-8">
<title>Project Title Here</title>
<link rel="stylesheet" href="https://fonts.googleapis.com/css2?family=Arimo:wght@400;700&display=swap">
<style>
  :root {
    --brand-blue: #0a6fc4;
    --brand-blue-dark: #0054a0;
    --brand-blue-light: #4c9ae0;
    --title-grey: #3a3a3a;
    --text-grey: #2b2b2b;
    --rule-grey: #e2e5ea;
    --floor-top: #d9d9d9;
    --floor-front: #a9a9a9;
    --white: #ffffff;
  }
  * { box-sizing: border-box; margin: 0; padding: 0; }
  html, body { width: 1200px; height: 900px; overflow: hidden; }
  body {
    font-family: "Arimo", Arial, sans-serif;
    background: var(--white);
    position: relative;
  }
  .slide { position: relative; width: 1200px; height: 900px; overflow: hidden; }
  .backdrop-photo {
    position: absolute; left: 0; top: 0; width: 1200px; height: 520px;
    background:
      radial-gradient(ellipse 520px 260px at 300px 90px, rgba(200,205,215,0.35), transparent 70%),
      radial-gradient(ellipse 380px 200px at 1000px 340px, rgba(170,195,225,0.28), transparent 70%),
      linear-gradient(180deg, #eef0f4 0%, #f7f8fa 60%, #ffffff 100%);
  }
  .slide-header {
    position: absolute; left: 0; top: 0; width: 1200px; height: 99px;
    border-bottom: 2px solid var(--rule-grey);
    background: rgba(255,255,255,0.55);
  }
  .project-title {
    position: absolute; left: 51px; top: 20px;
    font-size: 46px; font-weight: 700; letter-spacing: -0.5px;
    color: var(--title-grey);
  }
  .project-title .accent { color: var(--brand-blue); }
  .org-mark {
    position: absolute; right: 14px; top: 10px;
    display: flex; align-items: flex-start; gap: 12px;
  }
  .org-mark .org-square {
    width: 24px; height: 24px; background: var(--brand-blue); margin-top: 20px;
  }
  .org-mark .org-name {
    font-size: 21px; font-weight: 700; line-height: 27px;
    color: var(--title-grey); text-align: right; padding-top: 16px;
  }
  .section-heading {
    position: absolute; left: 77px; top: 137px;
    font-size: 25px; font-weight: 400; color: var(--text-grey);
  }
  .body-copy {
    position: absolute; left: 78px; top: 198px; width: 1070px;
    font-size: 19px; line-height: 33px; color: var(--text-grey);
  }
  .bar-chart { position: absolute; left: 0; top: 0; }
  .slide-footer {
    position: absolute; left: 0; top: 850px; width: 1200px; height: 50px;
    background: var(--brand-blue);
    color: var(--white); font-size: 20px;
    display: flex; align-items: center; justify-content: space-between;
    padding: 0 14px 0 23px;
  }
</style>
</head>
<body>
<main class="slide">
  <div class="backdrop-photo" role="img" aria-label="Faint healthcare photograph fading into the slide background"></div>

  <header class="slide-header">
    <h1 class="project-title"><span class="accent">Project</span> Title Here</h1>
    <div class="org-mark">
      <div class="org-name">Marrowfield and Kelton<br>Health Commissioning Board</div>
      <div class="org-square"></div>
    </div>
  </header>

  <h2 class="section-heading">Lorem ipsum dolor sit ipsum Lorem ipsum dolor sit ipsum Lorem ipsum</h2>

  <p class="body-copy">Lorem ipsum dolor sit ipsum Lorem ipsum dolor sit ipsum Lorem ipsum&nbsp; Lorem ipsum dolor sit ipsum Lorem ipsum dolor sit ipsum Lorem ipsum Lorem ipsum dolor sit ipsum Lorem ipsum dolor sit ipsum Lorem ipsum&nbsp; Lorem ipsum dolor sit ipsum Lorem ipsum dolor sit ipsum Lorem ipsum Lorem ipsum dolor sit ipsum Lorem ipsum dolor sit ipsum Lorem ipsum dolor sit ipsum Lorem ipsum&nbsp; Lorem ipsum dolor sit ipsum Lorem ipsum dolor sit ipsum Lorem ipsum Lorem ipsum Lorem ipsum dolor sit ipsum Lorem ipsum dolor sit ipsum.</p>

  <svg class="bar-chart" width="1200" height="900" viewBox="0 0 800 600" aria-label="Bar chart with seven bars">
    <g class="chart-floor">
      <polygon points="53,510 755,510 755,498 66,498" fill="var(--floor-top)"/>
      <rect x="53" y="510" width="702" height="10" fill="var(--floor-front)"/>
    </g>
    <g class="chart-bars">
      <!-- bar 1 -->
      <polygon points="70,342 82,331 145,331 133,342" fill="var(--brand-blue-light)"/>
      <polygon points="133,342 145,331 145,500 133,511" fill="var(--brand-blue-dark)"/>
      <rect x="70" y="342" width="63" height="169" fill="var(--brand-blue)"/>
      <!-- bar 2 -->
      <polygon points="174,480 186,473 249,473 237,480" fill="var(--brand-blue-light)"/>
      <polygon points="237,480 249,473 249,504 237,511" fill="var(--brand-blue-dark)"/>
      <rect x="174" y="480" width="63" height="31" fill="var(--brand-blue)"/>
      <!-- bar 3 -->
      <polygon points="268,484 280,478 343,478 331,484" fill="var(--brand-blue-light)"/>
      <polygon points="331,484 343,478 343,505 331,511" fill="var(--brand-blue-dark)"/>
      <rect x="268" y="484" width="63" height="27" fill="var(--brand-blue)"/>
      <!-- bar 4 -->
      <polygon points="361,441 373,429 436,429 424,441" fill="var(--brand-blue-light)"/>
      <polygon points="424,441 436,429 436,499 424,511" fill="var(--brand-blue-dark)"/>
      <rect x="361" y="441" width="63" height="70" fill="var(--brand-blue)"/>
      <!-- bar 5 -->
      <polygon points="465,410 477,398 546,398 534,410" fill="var(--brand-blue-light)"/>
      <polygon points="534,410 546,398 546,499 534,511" fill="var(--brand-blue-dark)"/>
      <rect x="465" y="410" width="69" height="101" fill="var(--brand-blue)"/>
      <!-- bar 6 -->
      <polygon points="571,484 583,479 646,479 634,484" fill="var(--brand-blue-light)"/>
      <polygon points="634,484 646,479 646,506 634,511" fill="var(--brand-blue-dark)"/>
      <rect x="571" y="484" width="63" height="27" fill="var(--brand-blue)"/>
      <!-- bar 7 -->
      <polygon points="666,495 678,492 741,492 729,495" fill="var(--brand-blue-light)"/>
      <polygon points="729,495 741,492 741,507 729,510" fill="var(--brand-blue-dark)"/>
      <rect x="666" y="495" width="63" height="15" fill="var(--brand-blue)"/>
    </g>
  </svg>

  <footer class="slide-footer">
    <span class="footer-text">Footer Text here</span>
    <span class="page-number">Page No. : 01</span>
  </footer>
</main>
</body>
</html>
```